Flyer-Design für Organisation von Golf Short Trips
Wir organisieren Golf Short Trips für Golfer aller Altersklassen. Hierfür sind wir auf der Suche nach einem minimalistischem und gleichzeitig hochwertigen Flyer/ Broschüre welches unsere wesentlichen Merkmale verkörpert.
Wir sind ein junges Unternehmen welches sich durch folgende Eigenschaften am besten beschreiben lässt: Innovativ, Disruptiv, Exklusiv, Produktiv, Modern. Diese Unternehmensphilosophie soll durch unseren Flyer erkennbar werden.
We organize golf short trips for golfers of all ages. For this we are looking for a minimalist and at the same time high quality flyer/ broschure which embodies our essential characteristics.
We are a young company which can be best described by the following characteristics: Innovative, Disruptive, Exclusive, Productive, Modern. This corporate philosophy should be recognizable through our flyer.
If possible use:
GRAU: #a2a4aa
GRÜN: #002F01
(SENFGELB: #cfa600)
Format: 138 x 297 / Two Pages (front/back)
So far, we have been working mainly with the Open Sans font.
Underground also Playfair styles. However, we would be happy to receive suggestions from you regarding the fonts.
!!! Please take the text specifications from the attached template: -> flyer_din_a5_hoch_tiefgruen.de.jpeg !!!
The design in general can be created by the designer at his own discretion.
A total of 3 logos must be included in the flyer. That of our company (medium size), the hotel group (small) and the golf course (small).
A small profile picture of the respective trainer should be placed on the front.
All textual content can be accessed via the following link: https://notizwerk-example.net/dokument/7Qx3LmRt9VbWz2KcHnPa5YsEu8JdGfTo4iXkNrBq/edit?usp=sharing

```html
<!DOCTYPE html>
<html lang="de">
<head>
<meta charset="utf-8">
<title>Golf Short Trip Flyer</title>
<link href="https://fonts.googleapis.com/css2?family=Open+Sans:ital,wght@0,300;0,400;0,600;0,700;0,800;1,400&family=PT+Sans+Narrow:wght@400;700&display=swap" rel="stylesheet">
<style>
:root{
  --green:#002f01;
  --green-dark:#1c3522;
  --stage:#3c5143;
  --gold:#cfa600;
  --grey:#a2a4aa;
  --grey-light:#d6d7da;
  --field:#ebecee;
  --white:#ffffff;
  --text:#222;
}
*{margin:0;padding:0;box-sizing:border-box}
html,body{width:696px;height:1200px;overflow:hidden}
body{background:var(--stage);position:relative;font-family:"Open Sans",sans-serif}
.page{position:absolute;top:375px;width:320px;height:450px;background:var(--white);overflow:hidden}
.page--front{left:16px}
.page--back{left:360px}
.abs{position:absolute}
.spaced{letter-spacing:.32em;text-transform:uppercase}

/* front */
.badge{position:absolute}
.club-box{left:112px;top:0;width:92px;height:97px;background:var(--grey-light);display:flex;align-items:center;justify-content:center}
.club-name{font-family:"Open Sans",sans-serif;font-weight:700;font-size:11px;color:var(--green);letter-spacing:.12em;text-transform:uppercase}
.club-line{left:0;width:100%;text-align:center;color:var(--grey);font-size:8.5px;font-weight:300;line-height:10px}
.course-photo{left:0;top:138px;width:320px;height:128px;background:linear-gradient(180deg,#eef0e6 0%,#dfe6c6 22%,#a9c068 45%,#7d9a3a 62%,#c9b48b 82%,#b9a27a 100%)}
.golf-word{left:0;top:176px;width:320px;text-align:center;font-weight:800;font-size:84px;line-height:90px;color:rgba(255,255,255,.72);letter-spacing:-.01em}
.trip-band{left:0;top:266px;width:320px;height:40px;background:var(--green-dark);border-top:1px solid #d9ddd5;display:flex;align-items:center;justify-content:center;color:var(--white);font-weight:800;font-size:19px;letter-spacing:.32em}
.trip-rule{left:0;top:307px;width:320px;height:3px;background:var(--gold)}
.field-label{left:22px;font-size:8px;line-height:9.5px;color:var(--grey);letter-spacing:.06em;text-transform:uppercase}
.field-label b{font-weight:700}
.field-label--gold{color:var(--gold)}
.field{background:var(--field);height:14px}
.tagline{left:0;top:403px;width:320px;text-align:center;font-size:6px;line-height:8px;color:var(--grey)}
.relax-bar{left:60px;top:434px;width:199px;height:16px;background:var(--gold);color:var(--white);font-size:6.5px;display:flex;align-items:center;justify-content:center}

/* back */
.schedule-bg{left:0;top:80px;width:180px;height:185px;background:linear-gradient(180deg,rgba(255,255,255,1) 0%,rgba(232,238,220,.9) 50%,rgba(214,224,196,.9) 100%)}
.services-photo{left:179px;top:0;width:141px;height:265px;background:linear-gradient(180deg,#8e918f 0%,#7a7f7a 40%,#6f756f 100%)}
.lobby-photo{left:0;top:265px;width:179px;height:185px;background:linear-gradient(160deg,#cfcbc4 0%,#a89c8a 45%,#5a5752 75%,#3d3b39 100%)}
.club-box--small{left:137px;top:0;width:42px;height:46px;background:var(--grey-light);display:flex;align-items:center;justify-content:center}
.club-box--small .club-name{font-size:6px;letter-spacing:.06em}
.section-title{font-size:8.5px;letter-spacing:.42em;color:var(--grey);font-weight:400}
.section-title--light{color:var(--white)}
.section-rule{width:24px;height:2px;background:var(--gold)}
.day-title{left:22px;font-size:6.5px;font-weight:700;letter-spacing:.32em;color:var(--text)}
.day-list{left:22px;list-style:none;font-family:"PT Sans Narrow",sans-serif;font-size:6.6px;line-height:10.3px;color:var(--text)}
.trainer-photo{left:159px;top:107px;width:28px;height:28px;border-radius:50%;background:radial-gradient(circle,#c9a688 0%,#7c9a62 100%);border:1.5px solid var(--white)}
.trainer-caption{left:118px;top:129px;font-size:5.3px;line-height:6.6px;font-style:italic;color:var(--grey)}
.services{left:197px;top:68px;list-style:none;font-family:"PT Sans Narrow",sans-serif;font-weight:700;font-size:7.2px;line-height:12.4px;color:var(--white)}
.services .gap{height:16px}
.price-box{left:91px;top:256px;width:139px;height:56px;background:var(--green-dark);color:var(--white);text-align:center;padding-top:6px}
.price-main{font-size:7.8px;line-height:9px;font-weight:400}
.price-sub{font-size:7px;margin-top:3px}
.price-note{font-size:5px;margin-top:1px}
.hotel-name{left:236px;top:301px;width:40px;text-align:center;font-family:"Open Sans",sans-serif;font-weight:600;font-size:6px;color:#6b2a5a}
.signup{left:182px;width:138px;text-align:center;font-family:"PT Sans Narrow",sans-serif;font-size:6.3px;color:var(--text)}
.signup-title{font-family:"Open Sans",sans-serif;font-weight:700;font-size:6.5px;letter-spacing:.4em}
.signup-link{font-weight:700}
.signup-bar{left:112px;top:441px;width:92px;height:9px;background:var(--gold)}
</style>
</head>
<body>

<!-- Front page -->
<section class="page page--front">
  <svg class="badge" style="left:13px;top:18px" width="58" height="58" viewBox="0 0 58 58" aria-hidden="true">
    <circle cx="29" cy="29" r="28" fill="var(--green-dark)" stroke="#d9d2a8" stroke-width="1.5"/>
    <circle cx="29" cy="29" r="18" fill="var(--white)"/>
    <text x="29" y="33" text-anchor="middle" font-family="Open Sans, sans-serif" font-weight="700" font-size="11" fill="var(--gold)">10%</text>
  </svg>

  <div class="abs club-box"><span class="club-name">Hainbuch</span></div>

  <p class="abs club-line spaced" style="top:110px">Golf &amp; Country</p>
  <p class="abs club-line spaced" style="top:120px">Hainbuch Luxembourg</p>

  <div class="abs course-photo" role="img" aria-label="Foto eines Golfplatzes mit Bunker und Bäumen im Morgenlicht"></div>
  <div class="abs golf-word">GOLF</div>

  <div class="abs trip-band">SHORT TRIP</div>
  <div class="abs trip-rule"></div>

  <p class="abs field-label" style="top:320px"><b>Erster</b><br>Reisezeitraum:</p>
  <div class="abs field" style="left:111px;top:321px;width:188px"></div>

  <p class="abs field-label" style="top:344px"><b>Zweiter</b><br>Reisezeitraum:</p>
  <div class="abs field" style="left:111px;top:348px;width:188px"></div>

  <p class="abs field-label field-label--gold" style="top:372px"><b>Early Bird</b><br>nur bis:</p>
  <div class="abs field" style="left:85px;top:373px;width:214px"></div>

  <p class="abs tagline spaced">Golf Short Trips by tiefgruen.de<br>Eine Klasse für sich</p>

  <div class="abs relax-bar spaced">Stay, Play &amp; Relax</div>
</section>

<!-- Back page -->
<section class="page page--back">
  <div class="abs schedule-bg" role="img" aria-label="Blasses Foto eines Golfplatzes als Hintergrund"></div>
  <div class="abs services-photo" role="img" aria-label="Grau getöntes Foto der Hotelanlage am Golfplatz"></div>
  <div class="abs lobby-photo" role="img" aria-label="Foto der Hotellobby mit Empfangstresen"></div>

  <div class="abs club-box--small"><span class="club-name">Hainbuch</span></div>

  <h2 class="abs section-title" style="left:22px;top:37px">ABLAUFPLAN</h2>
  <div class="abs section-rule" style="left:22px;top:52px"></div>

  <h3 class="abs day-title" style="top:66px">TRAININGSTAG 1</h3>
  <ul class="abs day-list" style="top:79px">
    <li>15.00 Uhr: Get-Together im Golf-Club Hainbuch</li>
    <li>16.00 Uhr: Trainingsstart auf der Driving Range mit Jonas Wendt</li>
    <li>19.30 Uhr: Abendessen im Hotelrestaurant</li>
  </ul>

  <div class="abs trainer-photo" role="img" aria-label="Profilfoto des Golftrainers"></div>
  <p class="abs trainer-caption">Jonas Wendt<br>Golf Professional</p>

  <h3 class="abs day-title" style="top:120px">TRAININGSTAG 2</h3>
  <ul class="abs day-list" style="top:133px">
    <li>ab 7.00 Uhr: Frühstück</li>
    <li>ca. 8.00 Uhr: Trainingsstart</li>
    <li>ab 8.30 Uhr: 18-Loch Runde mit Jonas Wendt</li>
    <li>ab 16.00 Uhr: freie Zeit</li>
    <li>ab 19.00 Uhr: Abendessen im Hotelrestaurant</li>
  </ul>

  <h3 class="abs day-title" style="top:194px">TRAININGSTAG 3</h3>
  <ul class="abs day-list" style="top:207px">
    <li>ab 7.00 Uhr Frühstück</li>
    <li>ca. 8.00 Uhr Trainingsstart</li>
    <li>ab 8.30 Uhr 18-Loch Runde mit Jonas Wendt</li>
    <li>ca. 15.00 Uhr Abreise</li>
  </ul>

  <h2 class="abs section-title section-title--light" style="left:197px;top:37px">LEISTUNGEN</h2>
  <div class="abs section-rule" style="left:197px;top:52px"></div>
  <ul class="abs services">
    <li>2 Übernachtungen im Hotel Lindenhof</li>
    <li>Hainbuch (inkl. reichhaltigem</li>
    <li>Frühstücksbuffet)</li>
    <li>Kostenlose Parkplätze</li>
    <li class="gap"></li>
    <li>2 x Greenfee auf dem Championship</li>
    <li>Course Hainbuch</li>
    <li>Tägliche Driving Range - Nutzung</li>
    <li>unlimited Rangeballs</li>
    <li>-10% Proshop Discount</li>
    <li>reservierte Abschlagszeiten</li>
    <li>Tischreservierung</li>
    <li>Betreuung und Golfprogramm mit</li>
    <li>Jonas Wendt</li>
  </ul>

  <div class="abs price-box">
    <p class="price-main">TEILNAHMEGEBÜHR AB<br><span style="letter-spacing:.06em">AB 699,00€ P.P.</span></p>
    <p class="price-sub">Einzelzimmerzuschlag + 125,00€*</p>
    <p class="price-note">*Von Aktionen ausgeschlossen</p>
  </div>

  <svg class="badge" style="left:262px;top:252px" width="42" height="42" viewBox="0 0 58 58" aria-hidden="true">
    <circle cx="29" cy="29" r="28" fill="var(--green-dark)" stroke="#d9d2a8" stroke-width="1.5"/>
    <circle cx="29" cy="29" r="18" fill="var(--white)"/>
    <text x="29" y="33" text-anchor="middle" font-family="Open Sans, sans-serif" font-weight="700" font-size="11" fill="var(--gold)">10%</text>
  </svg>

  <p class="abs hotel-name">Lindenhof</p>

  <p class="abs signup signup-title" style="top:329px">ANMELDUNG</p>
  <p class="abs signup" style="top:343px">unter:</p>
  <p class="abs signup signup-link" style="top:357px">www.tiefgruen.de oder buchung@tiefgruen.de</p>
  <p class="abs signup" style="top:378px">Bis zu 4 Wochen vorher kostenfrei stornieren</p>
  <p class="abs signup" style="top:398px">Meldeschluss</p>
  <div class="abs field" style="left:193px;top:413px;width:116px"></div>

  <div class="abs signup-bar"></div>
</section>

</body>
</html>
```